Consulting Company PowerPoint Template Design

We are looking for an updated PowerPoint template design or our 55 person energy consulting firm (K7) based in San Francisco (www.kaysev.example). We would like two versions of the same PowerPoint template in a 16:9 and 4:3 format with our existing logo.

We have an existing color scheme and template and are seeking your help to polish/update the template design for wide format and create a flexible template that is easy to use with content from Excel and Word. Our current template, and a couple of examples that we like are attached.

Specific requests include:

• Dark background for slide title
• A narrow section header
• Maximizing white space for content
• A limited number of well designed Master template layouts to choose from
• A selection of title and section header slides that are not San Francisco specific with some variety to chose from ideally with a focus on energy or nature, graphics/visuals.

For examples of energy specific templates see:
https://www.brightfolio.example/energy/powerpoint-templates/0.html

Requirements
Must have
• Must use our logo but open to other designs, fonts, and styles for the PowerPoint template.
• Please use our existing color scheme found in the attached Excel file.
• Also we would like the ability to easily copy and paste from our existing/original template to the new template. In other words we would like backward compatibility to apply the new template format to our old PowerPoints that use our existing template.

```html
<!DOCTYPE html>
<html lang="en">
<head>
<meta charset="utf-8">
<title>K7 Slide – Focus Areas</title>
<link href="https://fonts.googleapis.com/css2?family=Open+Sans:wght@400;600;700&family=Titillium+Web:wght@400;600;700&display=swap" rel="stylesheet">
<style>
  :root {
    --navy: #0d4b6c;
    --gold: #d9b66f;
    --gold-text: #d9b66f;
    --cream: #f4e6c8;
    --white: #ffffff;
  }
  html, body {
    margin: 0;
    padding: 0;
    width: 1200px;
    height: 900px;
    overflow: hidden;
    background: var(--white);
  }
  .slide {
    position: relative;
    width: 1200px;
    height: 900px;
    overflow: hidden;
    background: var(--white);
    font-family: "Open Sans", Arial, sans-serif;
  }
  .slide-header { position: absolute; left: 0; top: 0; width: 1200px; height: 90px; }
  .slide-header svg { position: absolute; left: 0; top: 0; }
  .slide-title {
    position: absolute;
    left: 18px;
    top: 10px;
    margin: 0;
    font-family: "Open Sans", Arial, sans-serif;
    font-weight: 600;
    font-size: 31px;
    letter-spacing: 0.3px;
    color: var(--white);
  }
  .slide-title .accent { color: var(--gold-text); }
  .brand {
    position: absolute;
    left: 1110px;
    top: 6px;
    width: 78px;
    height: 78px;
    border-radius: 50%;
    background: var(--white);
    border: 4px solid var(--navy);
    box-sizing: border-box;
    display: flex;
    align-items: center;
    justify-content: center;
    font-family: "Open Sans", Arial, sans-serif;
    font-weight: 700;
    font-size: 28px;
    color: var(--navy);
  }
  .focus-row { position: absolute; left: 25px; width: 1132px; height: 168px; }
  .focus-row svg.shape { position: absolute; left: 0; top: 0; }
  .focus-icon { position: absolute; left: 98px; top: 22px; width: 52px; height: 52px; }
  .focus-label {
    position: absolute;
    left: 0;
    width: 248px;
    top: 104px;
    text-align: center;
    font-family: "Open Sans", Arial, sans-serif;
    font-size: 26px;
    color: var(--white);
  }
  .focus-copy { position: absolute; left: 336px; top: 24px; width: 770px; }
  .focus-copy h2 {
    margin: 0 0 4px;
    font-family: "Open Sans", Arial, sans-serif;
    font-weight: 700;
    font-size: 30px;
    line-height: 40px;
    color: var(--white);
  }
  .focus-copy p {
    margin: 0;
    font-family: "Titillium Web", Arial, sans-serif;
    font-size: 22px;
    line-height: 33px;
    color: var(--white);
  }
  .slide-footer { position: absolute; left: 0; top: 855px; width: 1200px; height: 45px; background: var(--navy); }
  .footer-name {
    position: absolute;
    left: 9px;
    top: 5px;
    font-family: "Open Sans", Arial, sans-serif;
    font-weight: 700;
    font-size: 24px;
    color: var(--white);
  }
  .page-tab { position: absolute; left: 1088px; top: 3px; }
  .page-number {
    position: absolute;
    left: 1138px;
    top: 10px;
    font-family: "Open Sans", Arial, sans-serif;
    font-size: 20px;
    color: var(--navy);
  }
</style>
</head>
<body>
<div class="slide">

  <header class="slide-header">
    <svg width="1200" height="90" viewBox="0 0 1200 90" aria-hidden="true">
      <rect x="0" y="0" width="1200" height="62" fill="var(--navy)"/>
      <polygon points="0,66 1088,66 1104,76 0,76" fill="var(--gold)"/>
    </svg>
    <h1 class="slide-title"><span class="accent">PROJECT</span> TITLE HERE</h1>
    <div class="brand">K7</div>
  </header>

  <section class="focus-row" style="top:159px">
    <svg class="shape" width="1132" height="168" viewBox="0 0 1132 168" aria-hidden="true">
      <polygon points="250,0 1132,0 1132,168 250,168 304,84" fill="var(--gold)"/>
      <polygon points="0,0 244,0 298,84 244,168 0,168" fill="var(--navy)"/>
    </svg>
    <svg class="focus-icon" viewBox="0 0 52 52" fill="none" stroke="var(--white)" stroke-width="2.4" aria-hidden="true">
      <circle cx="26" cy="12" r="8"/>
      <circle cx="26" cy="12" r="3"/>
      <line x1="26" y1="20" x2="26" y2="38"/>
      <circle cx="26" cy="36" r="12"/>
      <circle cx="26" cy="36" r="6"/>
      <line x1="8" y1="36" x2="44" y2="36"/>
      <line x1="26" y1="46" x2="26" y2="52"/>
    </svg>
    <div class="focus-label">Focus area</div>
    <div class="focus-copy">
      <h2>Subtext Title Here</h2>
      <p>Rise Forward contributes to the eradication of extreme poverty by partnering with governments and global agencies to ensure that, through policy</p>
    </div>
  </section>

  <section class="focus-row" style="top:382px">
    <svg class="shape" width="1132" height="168" viewBox="0 0 1132 168" aria-hidden="true">
      <polygon points="250,0 1132,0 1132,168 250,168 304,84" fill="var(--gold)"/>
      <polygon points="0,0 244,0 298,84 244,168 0,168" fill="var(--navy)"/>
    </svg>
    <svg class="focus-icon" viewBox="0 0 52 52" fill="none" stroke="var(--white)" stroke-width="2.4" aria-hidden="true">
      <path d="M18 32 C12 28 10 22 12 16 C14 9 20 6 26 6 C32 6 38 9 40 16 C42 22 40 28 34 32 L34 38 L18 38 Z"/>
      <line x1="19" y1="42" x2="33" y2="42"/>
      <line x1="20" y1="46" x2="32" y2="46"/>
      <path d="M22 38 L22 26 L26 22 L30 26 L30 38"/>
    </svg>
    <div class="focus-label">Focus area</div>
    <div class="focus-copy">
      <h2>Subtext Title Here</h2>
      <p>Rise Forward contributes to the eradication of extreme poverty by partnering with governments and global agencies to ensure that, through policy</p>
    </div>
  </section>

  <section class="focus-row" style="top:603px">
    <svg class="shape" width="1132" height="170" viewBox="0 0 1132 170" aria-hidden="true">
      <polygon points="250,0 1132,0 1132,170 250,170 304,85" fill="var(--gold)"/>
      <polygon points="0,0 244,0 298,85 244,170 0,170" fill="var(--navy)"/>
    </svg>
    <svg class="focus-icon" viewBox="0 0 52 52" aria-hidden="true">
      <path d="M10 44 C4 44 1 40 1 35 C1 30 5 26 10 27 C10 20 16 15 23 16 C27 10 36 10 40 16 C46 16 51 21 50 28 C52 32 51 44 42 44 Z" fill="var(--white)"/>
    </svg>
    <div class="focus-label">Focus area</div>
    <div class="focus-copy">
      <h2>Subtext Title Here</h2>
      <p>Rise Forward contributes to the eradication of extreme poverty by partnering with governments and global agencies to ensure that, through policy</p>
    </div>
  </section>

  <footer class="slide-footer">
    <div class="footer-name">Kaysev Energy Economics</div>
    <svg class="page-tab" width="112" height="42" viewBox="0 0 112 42" aria-hidden="true">
      <path d="M0,0 L112,0 L112,42 L26,42 C18,30 12,8 0,0 Z" fill="var(--cream)"/>
    </svg>
    <div class="page-number">01</div>
  </footer>

</div>
</body>
</html>
```